Web Design Project

need a website, logo and a matching business Card for design studio. i have a company that works with many companies and i want to offer design services that will be outsourced to craftflock.

this website is totally for the design services. i need it to be simple but very catcgy and trendy, yet MUST BE ELEGENT.

you being a designer will know best what do i require in this website and how it should look and feel..

i dont need many pages, most of the selling work to clients will be face to face, this is just for them to view the sample works.

the company is called "Corvelin, Vividra Studio", so pages i need are: 1- the Studio 2- Folios 3- Contact us( will include company informaiton, and online contact form that should have a drop-down list of all types of designs.

main focus is the folios pages, it needs to have samples of works, the classification of works should be on two basis, by type of design and by designer. client should be able to select a certain designer and send an inquiry. if the customer does that, then i should get all client details and the designer should get a notification that he has been requested though no contact details of client should be given to designer as i want to make sure that those jobs are given to designer through craft flock and this is an invitation for any designer who care to put his works on the website. next to that, if the customer requires a job online then we need to get information on how design should feel and look.

please quote your price to include the website and business card design, A3 head letter and envelope.

Please provide a mock up of your design or a briefing an initial design before asking to be announced as the winner.

my customers are general managers and decision makers.

Business

• ability to filiter works based on type or designer. and website must offer all types of designs included here

```html
<!DOCTYPE html>
<html lang="en">
<head>
<meta charset="utf-8">
<title>Corvelin Vividra Studio</title>
<link rel="stylesheet" href="https://fonts.googleapis.com/css2?family=Questrial&family=Arimo:wght@400;700&display=swap">
<style>
:root{
  --ink:#2b2b2b;
  --heading-blue:#1f5a96;
  --body-text:#333;
  --muted:#7a7a7a;
  --accent-red:#c8102e;
  --panel:#ffffff;
  --card-top:#f7f7f7;
  --card-bottom:#e6e6e6;
  --field-border:#c9c9c9;
  --footer:#3a3a3a;
  --footer-bottom:#343434;
  --footer-text:#d6d6d6;
  --submit-top:#3fb6f2;
  --submit-bottom:#0a78c4;
}
*{box-sizing:border-box;margin:0;padding:0}
html,body{width:1194px;height:1200px;overflow:hidden}
body{position:relative;font-family:"Arimo",Arial,sans-serif;color:var(--body-text);background:#f1eef0}
.hero-art{position:absolute;left:0;top:0;width:1194px;height:910px;
  background:
   radial-gradient(ellipse 500px 160px at 700px 420px,rgba(228,120,170,.25),transparent 70%),
   radial-gradient(ellipse 600px 140px at 500px 860px,rgba(220,110,160,.35),transparent 70%),
   radial-gradient(ellipse 300px 260px at 1150px 500px,rgba(200,90,150,.25),transparent 70%),
   radial-gradient(circle 260px at 120px 60px,rgba(255,255,255,.8),transparent 70%),
   linear-gradient(180deg,#f4f1f3 0%,#ece6ea 60%,#e9dfe5 100%)}
.abs{position:absolute}
.brand-mark{left:37px;top:79px;width:170px;height:73px;background:#3a3a3a}
.brand-name{left:240px;top:83px;font-family:"Questrial",sans-serif;font-size:43px;color:var(--ink);letter-spacing:.2px}
.social{top:39px;width:33px;height:33px;border-radius:6px;background:#2f5f9e;color:#fff;font-size:8px;display:flex;align-items:center;justify-content:center;font-family:"Arimo",sans-serif}
.social.facet{left:1065px}
.social.chirrup{left:1127px;background:#37aee0}
.search-panel{top:217px;width:402px;height:117px;background:var(--panel);border-radius:6px;box-shadow:0 2px 6px rgba(0,0,0,.2)}
.search-panel.design{left:134px}
.search-panel.job{left:636px}
.select{position:absolute;left:19px;top:42px;width:371px;height:33px;border:1px solid #b9b9b9;background:linear-gradient(#fff,#f2f2f2);font-size:13px;color:#666;padding:0 16px;line-height:31px;box-shadow:inset 0 2px 2px rgba(0,0,0,.15)}
.select svg{position:absolute;right:3px;top:4px}
.main-panel{left:74px;top:398px;width:1059px;height:487px;background:rgba(255,255,255,.85);border-radius:5px;box-shadow:0 1px 4px rgba(0,0,0,.15)}
.col-title{top:434px;font-family:"Questrial",sans-serif;font-size:27px;color:var(--heading-blue)}
.card{top:485px;width:289px;height:352px;border-radius:4px;border:1px solid #dcdcdc;background:linear-gradient(var(--card-top),var(--card-bottom))}
.thumb{position:absolute;border:3px solid #fff;box-shadow:0 1px 3px rgba(0,0,0,.3)}
.thumb.rounded{border-radius:8px}
.blurb{position:absolute;width:130px;font-size:12.5px;line-height:19px;color:var(--body-text)}
.more{position:absolute;font-size:12.5px;color:var(--accent-red)}
.field{position:absolute;left:28px;width:235px;height:35px;border:1px solid var(--field-border);border-radius:4px;background:linear-gradient(#fff,#ececec);font-size:12.5px;color:#777;padding:10px 17px}
.submit{position:absolute;left:162px;top:285px;width:94px;height:39px;border-radius:7px;border:2px solid #9aa7b0;background:linear-gradient(var(--submit-top),var(--submit-bottom));color:#fff;font-size:16px;text-align:center;line-height:35px}
.footer{left:0;top:910px;width:1194px;height:216px;background:var(--footer)}
.footer-bottom{left:0;top:1132px;width:1194px;height:68px;background:var(--footer-bottom);border-top:1px solid #2a2a2a}
.footer-col{top:946px}
.footer-col h3{font-weight:400;font-size:16.5px;color:var(--footer-text);margin-left:1px;margin-bottom:17px}
.footer-col li{list-style:none;font-size:12.5px;color:var(--footer-text);height:25px;display:flex;align-items:center;gap:9px;margin-left:-4px}
.footer-col li::before{content:"›";font-size:17px;font-weight:700;line-height:1}
.footer-brand{left:894px;top:1029px;display:flex;align-items:center;gap:6px;font-family:"Questrial",sans-serif;font-size:17px;color:#7d7d7d}
.footer-brand span.mark{width:68px;height:30px;background:#555}
.copyright{left:0;top:1155px;width:1194px;text-align:center;font-size:12.5px;color:var(--footer-text)}
</style>
</head>
<body>
<div class="hero-art" role="img" aria-label="Soft abstract background of sketched pink and grey swirling strokes"></div>

<header>
  <div class="abs brand-mark" aria-hidden="true"></div>
  <h1 class="abs brand-name">Corvelin Vividra Studio</h1>
  <a class="abs social facet">Facet</a>
  <a class="abs social chirrup">Chirrup</a>
</header>

<div class="abs search-panel design"><div class="select">SEARCH BY DESIGN<svg width="17" height="23"><rect width="17" height="23" rx="2" fill="#c5d3ea"/><path d="M4 9l4.5 5 4.5-5" stroke="#2b4a80" stroke-width="2" fill="none"/></svg></div></div>
<div class="abs search-panel job"><div class="select">SEARCH BY JOB<svg width="17" height="23"><rect width="17" height="23" rx="2" fill="#c5d3ea"/><path d="M4 9l4.5 5 4.5-5" stroke="#2b4a80" stroke-width="2" fill="none"/></svg></div></div>

<main>
  <div class="abs main-panel"></div>

  <h2 class="abs col-title" style="left:118px">RECENT JOBS</h2>
  <h2 class="abs col-title" style="left:459px">Folios</h2>
  <h2 class="abs col-title" style="left:802px">Contact Us</h2>

  <section class="abs card" style="left:116px">
    <div class="thumb" style="left:14px;top:29px;width:93px;height:93px;background:linear-gradient(135deg,#2a3b5a,#a9b6cc 55%,#3d4656)" role="img" aria-label="Photo of a businessman touching a glowing globe"></div>
    <p class="blurb" style="left:130px;top:29px">Nunc varius facilisis eros. Sed rat. In in velit quis arcu ornare laoreet. luctus massa.</p>
    <a class="more" style="left:170px;top:134px">&gt;&gt;&nbsp; Read More</a>
    <div class="thumb" style="left:17px;top:180px;width:93px;height:93px;background:linear-gradient(160deg,#4a4a4a,#d8cdb8 60%,#2c3346)" role="img" aria-label="Photo of a businessman holding an umbrella"></div>
    <p class="blurb" style="left:130px;top:184px">Nunc varius facilisis eros. Sed rat. In in velit quis arcu ornare laoreet. luctus massa.</p>
    <a class="more" style="left:170px;top:288px">&gt;&gt;&nbsp; Read More</a>
  </section>

  <section class="abs card" style="left:456px">
    <div class="thumb rounded" style="left:17px;top:25px;width:122px;height:128px;background:radial-gradient(circle at 50% 45%,#8b7aa0,#3b3b3b 75%)" role="img" aria-label="Artwork of a dancer in a burst of paint"></div>
    <p class="blurb" style="left:156px;top:37px">Nunc varius facilisis eros. Sed rat. In in velit quis arcu ornare laoreet. luctus massa.</p>
    <div class="thumb rounded" style="left:19px;top:192px;width:122px;height:128px;background:linear-gradient(135deg,#e6b46a,#d77fb8 45%,#6fc6d8)" role="img" aria-label="Colourful artwork of a figure in glowing light"></div>
    <p class="blurb" style="left:156px;top:205px">Nunc varius facilisis eros. Sed rat. In in velit quis arcu ornare laoreet. luctus massa.</p>
  </section>

  <section class="abs card" style="left:799px">
    <div class="field" style="top:33px">Name</div>
    <div class="field" style="top:82px">Email ID</div>
    <div class="field" style="top:131px">Phone</div>
    <div class="field" style="top:180px;height:81px">Message</div>
    <div class="submit">Submit</div>
  </section>
</main>

<footer>
  <div class="abs footer"></div>
  <div class="abs footer-bottom"></div>
  <div class="abs footer-col" style="left:58px"><h3>About us</h3><ul><li>Loreum Ipsum dollar</li><li>Loreum Ipsum dollar</li><li>Loreum Ipsum dollar</li><li>Loreum Ipsum dollar</li><li>Loreum Ipsum dollar</li></ul></div>
  <div class="abs footer-col" style="left:272px"><h3>About us</h3><ul><li>Loreum Ipsum dollar</li><li>Loreum Ipsum dollar</li><li>Loreum Ipsum dollar</li><li>Loreum Ipsum dollar</li><li>Loreum Ipsum dollar</li></ul></div>
  <div class="abs footer-col" style="left:490px"><h3>About us</h3><ul><li>Loreum Ipsum dollar</li><li>Loreum Ipsum dollar</li><li>Loreum Ipsum dollar</li><li>Loreum Ipsum dollar</li><li>Loreum Ipsum dollar</li></ul></div>
  <div class="abs footer-col" style="left:706px"><h3>About us</h3><ul><li>Loreum Ipsum dollar</li><li>Loreum Ipsum dollar</li><li>Loreum Ipsum dollar</li><li>Loreum Ipsum dollar</li><li>Loreum Ipsum dollar</li></ul></div>
  <div class="abs footer-brand"><span class="mark"></span>Corvelin Vividra Studio</div>
  <p class="abs copyright">© 2012 Vividra Studio. All rights reserved.</p>
</footer>
</body>
</html>
```